Brinevale Yacht Management Full Page Ad Flyer

Yacht Management Package also includes the following periodic Monthly services:

Monthly full vessel systems checklist inspections
Diver For Hull Cleaning And Inspection Of Props, Shafts, and Zincs
Interior/Exterior Detailing and scheduled washdowns
Manage Haulout
Pump-out Services
On-call Captain and Crew Services
Updates

Need more time to provide more content to designers and the printing press template file.

Target Market(s)

Vessel owners, motor yachts, sailboats from 25 feet in length up to 125 feet in length. We do not do cruise ships or yachts larger than 125 feet. Someone who has their boat docked at their house or a local marina. We also offer mobile on-site services.

```html
<!DOCTYPE html>
<html lang="en">
<head>
<meta charset="utf-8">
<title>Brinevale Yacht Management – Monthly Services Ad</title>
<link href="https://fonts.googleapis.com/css2?family=Anton&family=Allura&family=Michroma&family=Roboto:wght@400&display=swap" rel="stylesheet">
<style>
  :root {
    --backdrop: #d6d6d6;
    --page-top: #d4dff1;
    --page-mid: #c9d8ef;
    --navy: #2153a5;
    --sky: #3a9fdc;
    --ink: #2a3346;
    --white: #ffffff;
    --hull: #f3f6fb;
    --hull-shade: #dfe6f1;
    --sea-light: #6f98cf;
    --sea-mid: #3567b0;
    --sea-deep: #1f4a90;
  }
  * { box-sizing: border-box; margin: 0; padding: 0; }
  html, body {
    width: 1200px; height: 2201px; overflow: hidden;
    background: var(--backdrop);
  }
  .ad-page {
    position: absolute; left: 100px; top: 406px;
    width: 1000px; height: 1388px; overflow: hidden;
    background: linear-gradient(180deg, var(--page-top) 0%, var(--page-mid) 50%, #dfe8f5 100%);
  }
  .hero-photo {
    position: absolute; left: 0; top: 700px; width: 1000px; height: 688px;
    z-index: 0;
    background:
      radial-gradient(ellipse 42% 34% at 90% 100%, var(--white) 0%, var(--white) 55%, rgba(255,255,255,0) 100%),
      linear-gradient(172deg, rgba(31,74,144,0) 0%, rgba(31,74,144,0) 64%, var(--sea-light) 70%, var(--sea-mid) 82%, var(--sea-deep) 100%),
      linear-gradient(158deg, rgba(201,216,239,0) 0%, var(--hull-shade) 14%, var(--white) 30%, var(--hull) 48%, var(--hull-shade) 62%, #cfdcee 70%);
  }
  .headline-yacht {
    position: absolute; left: 0; width: 100%; top: 92px; z-index: 2;
    text-align: center;
    font-family: "Anton", "Oswald", sans-serif; font-weight: 400;
    font-size: 206px; line-height: 1; letter-spacing: -2px;
    color: var(--navy);
    transform: scaleX(0.92);
  }
  .headline-script {
    position: absolute; left: 150px; top: 270px; z-index: 3;
    font-family: "Allura", cursive;
    font-size: 138px; line-height: 1;
    color: var(--sky);
    white-space: nowrap;
  }
  .headline-package {
    position: absolute; left: 502px; top: 370px; z-index: 2;
    font-family: "Michroma", sans-serif;
    font-size: 31px; letter-spacing: 15px; line-height: 1.2;
    color: var(--navy);
  }
  .services-band {
    position: absolute; left: 198px; top: 473px; z-index: 2;
    width: 604px; height: 62px;
    background: var(--navy);
    color: var(--white);
    font-family: "Michroma", sans-serif; font-weight: 400;
    font-size: 30px; letter-spacing: 2px;
    display: flex; align-items: center; justify-content: center;
  }
  .service-list {
    position: absolute; top: 596px; list-style: none; z-index: 2;
    font-family: "Roboto", sans-serif;
    font-size: 19px; line-height: 24px; color: var(--ink);
  }
  .service-list li {
    position: relative; padding-left: 28px; margin-bottom: 14px;
  }
  .service-list svg {
    position: absolute; left: 0; top: 5px; width: 14px; height: 14px;
  }
  .col-one { left: 100px; width: 280px; }
  .col-two { left: 396px; width: 270px; }
  .col-three { left: 668px; width: 300px; }
  .col-three li:first-child { margin-bottom: 12px; }
  .brand-name {
    position: absolute; left: 630px; top: 1290px; width: 310px; z-index: 2;
    text-align: center;
    font-family: "Michroma", sans-serif;
    font-size: 32px; letter-spacing: 3px;
    color: var(--navy);
  }
</style>
</head>
<body>
  <main class="ad-page">
    <div class="hero-photo" role="img" aria-label="White motor yacht cruising through deep blue sea with spray at the bow"></div>

    <h1 class="headline-yacht">YACHT</h1>
    <div class="headline-script">Management</div>
    <div class="headline-package">PACKAGE</div>

    <h2 class="services-band">MONTHLY SERVICES:</h2>

    <ul class="service-list col-one">
      <li><svg viewBox="0 0 14 14"><circle cx="7" cy="7" r="7" fill="var(--sky)"/><path d="M3.8 7.2l2.2 2.1 4.2-4.4" stroke="#fff" stroke-width="1.6" fill="none"/></svg>Monthly full<br>vessel systems checklist<br>inspections</li>
      <li><svg viewBox="0 0 14 14"><circle cx="7" cy="7" r="7" fill="var(--sky)"/><path d="M3.8 7.2l2.2 2.1 4.2-4.4" stroke="#fff" stroke-width="1.6" fill="none"/></svg>Diver For Hull Cleaning<br>And Inspection Of Props,<br>Shafts, and Zincs</li>
    </ul>
    <ul class="service-list col-two">
      <li><svg viewBox="0 0 14 14"><circle cx="7" cy="7" r="7" fill="var(--sky)"/><path d="M3.8 7.2l2.2 2.1 4.2-4.4" stroke="#fff" stroke-width="1.6" fill="none"/></svg>Interior/Exterior<br>Detailing and scheduled<br>washdowns</li>
      <li><svg viewBox="0 0 14 14"><circle cx="7" cy="7" r="7" fill="var(--sky)"/><path d="M3.8 7.2l2.2 2.1 4.2-4.4" stroke="#fff" stroke-width="1.6" fill="none"/></svg>Manage Haulout</li>
    </ul>
    <ul class="service-list col-three">
      <li><svg viewBox="0 0 14 14"><circle cx="7" cy="7" r="7" fill="var(--sky)"/><path d="M3.8 7.2l2.2 2.1 4.2-4.4" stroke="#fff" stroke-width="1.6" fill="none"/></svg>Pump-out Services</li>
      <li><svg viewBox="0 0 14 14"><circle cx="7" cy="7" r="7" fill="var(--sky)"/><path d="M3.8 7.2l2.2 2.1 4.2-4.4" stroke="#fff" stroke-width="1.6" fill="none"/></svg>On-call Captain<br>and Crew Services</li>
    </ul>

    <div class="brand-name">BRINEVALE</div>
  </main>
</body>
</html>
```